Advertising Material for Event

We are needing some advertising material done for an event. It can all be roughly the same except the two social media posts. We need:
- A banner
- A flyer
- 2 X social media posts

I have attached some examples of what we have done in the past. I have also attached a word document with the information.

Our colours are:
NAVY BLUE: Hex = #041E42 // RGB = 4 / 30 / 66 // CMYK = 100 / 90 / 13 / 68 // Pantone = 289 C
LIME GREEN: Hex = #97D700 // RGB = 151 / 215 / 0 // CMYK = 46 / 0 / 90 / 0 // Pantone = 375 C
WHITE

Our font are:
Avenir next regular, bold and demi bold
Freshman

Colors

Designer to choose colors to be used in the design.

Requirements
Must have
• Include photos provided. All info provided
Nice to have
• not cluttered

```html
<!DOCTYPE html>
<html lang="en">
<head>
<meta charset="utf-8">
<title>2022 Cheerleading Team Placements – Event Set</title>
<link href="https://fonts.googleapis.com/css2?family=Graduate&family=Nunito+Sans:wght@400;600;700;800;900&family=Oswald:wght@500;600&display=swap" rel="stylesheet">
<style>
  :root{
    --navy:#041E42;
    --navy-deep:#0a1526;
    --lime:#97D700;
    --green:#4f9c1d;
    --green-dark:#2f6e1b;
    --white:#ffffff;
    --silver:#e3e6e8;
    --photo-top:rgba(226,196,170,.55);
    --photo-bottom:rgba(20,36,64,.75);
  }
  *{box-sizing:border-box;margin:0;padding:0}
  html,body{width:1200px;height:4000px;overflow:hidden;background:var(--white)}
  body{position:relative;font-family:"Nunito Sans",sans-serif;color:var(--white)}
  .piece{position:absolute;overflow:hidden;box-shadow:0 6px 18px rgba(0,0,0,.25)}
  .abs{position:absolute}
  .photo{position:absolute;border-radius:40px 40px 18px 18px;
    background:linear-gradient(180deg,var(--photo-top),rgba(151,215,0,.35) 55%,var(--photo-bottom))}
  .display{font-family:"Graduate",serif;line-height:1;white-space:nowrap}
  .year{color:#6fbf1f;-webkit-text-stroke:3px var(--navy);letter-spacing:2px}
  .year-navy{color:var(--navy);-webkit-text-stroke:2px #274a7a;letter-spacing:2px}
  .title{color:var(--silver);-webkit-text-stroke:2px var(--navy);letter-spacing:2px}
  .sub{font-weight:800;white-space:nowrap;line-height:1}
  .band{position:absolute;background:var(--navy-deep);clip-path:polygon(2% 0,100% 0,98% 100%,0 100%);
    border-left:6px solid var(--lime);border-right:6px solid var(--lime);
    display:flex;flex-direction:column;justify-content:center;align-items:center;text-align:center;font-weight:800;line-height:1.3}
  .date-box{position:absolute;background:var(--white);color:var(--navy);border-radius:6px;display:flex;align-items:center;justify-content:center;flex-direction:column;font-weight:800;line-height:1}
  .date-box sup{font-size:.55em}
  .day-strip{position:absolute;background:var(--lime);color:var(--navy);border-radius:6px 0 0 6px;font-weight:800;display:flex;align-items:center;justify-content:center}
  .day-strip span{writing-mode:vertical-rl;transform:rotate(180deg);white-space:nowrap}
  .yr{position:absolute;font-family:"Oswald",sans-serif;font-weight:500;color:var(--lime);line-height:1;white-space:nowrap}
  .age{position:absolute;line-height:1.1;white-space:nowrap;font-weight:800}
  .age .label{color:var(--lime);font-weight:700}
  .age .label b{color:var(--white);font-weight:700}
  .strip{position:absolute;background:rgba(4,20,45,.9);display:flex;align-items:center;font-weight:700;white-space:nowrap}
  .price{color:var(--lime);font-weight:900}
  .tag{position:absolute;background:var(--lime);color:var(--navy);font-weight:800;display:flex;align-items:center;justify-content:center;white-space:nowrap;clip-path:polygon(3% 0,100% 0,97% 100%,0 100%)}
  .info-box{position:absolute;border:1px solid rgba(255,255,255,.7);text-align:center;display:flex;flex-direction:column;justify-content:center}
  .info-box .q{color:var(--lime);font-weight:700}
  .hl{color:var(--lime)}
  .footer{position:absolute;display:flex;align-items:center;white-space:nowrap;font-weight:600}
  .brand{font-weight:800;color:var(--white);letter-spacing:.5px}
  .icon{display:inline-block;vertical-align:middle}

  /* ---------- Flyer ---------- */
  .flyer{left:213px;top:193px;width:778px;height:1099px;
    background:radial-gradient(circle at 85% 8%,rgba(255,255,255,.35),transparent 18%),
      linear-gradient(180deg,#6bbd24 0%,#3e8e2a 25%,#14503a 45%,#0d2c48 60%,#0a1a2f 100%)}
  /* ---------- Banner ---------- */
  .banner{left:112px;top:1360px;width:980px;height:491px;
    background:radial-gradient(circle at 85% 25%,rgba(255,255,255,.3),transparent 20%),
      linear-gradient(180deg,#5fb21f 0%,#3d8a2a 38%,#123e44 62%,#0b1c33 100%)}
  /* ---------- Social posts ---------- */
  .social{width:834px;height:831px;
    background:radial-gradient(circle at 55% 18%,rgba(255,255,255,.35),transparent 14%),
      linear-gradient(165deg,#7cc423 0%,#3f8f26 35%,#1b4d4a 55%,#0d2446 75%,#091a33 100%)}
  .social-a{left:185px;top:1958px}
  .social-b{left:176px;top:2882px;transform-origin:0 0;transform:scale(1.022)}
  .social .panel{position:absolute;inset:0;background:var(--white);clip-path:polygon(0 137px,330px 137px,580px 771px,0 771px)}
  .social .topbar{position:absolute;left:0;top:0;width:400px;height:137px;background:var(--navy);clip-path:polygon(0 0,100% 0,82% 100%,0 100%)}
  .social .navy-band{position:absolute;left:0;background:var(--navy);clip-path:polygon(0 0,100% 0,96% 100%,0 100%)}
  .social .navy-band::after{content:"";position:absolute;right:0;top:0;width:14px;height:100%;background:var(--lime)}
  .social .dark{color:var(--navy)}
  .social .date-card{position:absolute;left:59px;top:464px;width:180px;height:78px;border:2px solid var(--navy);border-radius:6px;overflow:hidden;background:var(--white)}
  .social .date-card .day{position:absolute;left:8px;top:5px;font-size:13px;font-weight:700;line-height:1.1;white-space:nowrap}
  .social .date-card .num{font-size:30px;font-weight:900}
  .social .date-card .yr-block{position:absolute;right:0;top:0;width:84px;height:100%;background:var(--navy);display:flex;align-items:center;justify-content:center}
  .social .date-card .yr{position:static;font-size:36px}
  .social .times{left:256px;top:462px;line-height:1.15;font-weight:900;font-size:22px;white-space:nowrap}
</style>
</head>
<body>

<!-- ================= FLYER ================= -->
<section class="piece flyer">
  <div class="photo" role="img" aria-label="Cheerleader mid-air in a toe-touch jump" style="left:5px;top:64px;width:202px;height:78px;border-radius:40px"></div>
  <div class="photo" role="img" aria-label="Cheerleading stunt group lifting a flyer, left side" style="left:67px;top:282px;width:187px;height:358px"></div>
  <div class="photo" role="img" aria-label="Young cheerleader standing on a kneeling partner's back" style="left:315px;top:306px;width:156px;height:334px"></div>
  <div class="photo" role="img" aria-label="Cheerleading pyramid with a flyer held high, right side" style="left:595px;top:40px;width:183px;height:600px"></div>

  <div class="abs display year" style="left:0;width:778px;text-align:center;top:52px;font-size:100px">2022</div>
  <div class="abs display title" style="left:0;width:778px;text-align:center;top:160px;font-size:58px">CHEERLEADING</div>
  <div class="abs sub" style="left:0;width:778px;text-align:center;top:223px;font-size:34px">TEAM PLACEMENTS</div>

  <div class="band" style="left:20px;top:637px;width:740px;height:56px;font-size:17px">
    <span>Try out for a cheerleading team!</span>
    <span>Everyone is welcome and will be placed on a team, regardless of skill level.</span>
  </div>

  <div class="day-strip" style="left:48px;top:726px;width:20px;height:66px;font-size:9px"><span>SATURDAY</span></div>
  <div class="date-box" style="left:68px;top:726px;width:88px;height:66px;border-radius:0 6px 6px 0;font-size:36px">
    <span>11<sup>th</sup></span><span style="font-size:11px;margin-top:2px">DECEMBER</span>
  </div>
  <div class="yr" style="left:164px;top:729px;font-size:50px">2021</div>
  <div class="age" style="left:268px;top:730px"><div class="label" style="font-size:17px">11 YEARS <b>AND</b> UNDER</div><div style="font-size:30px">3:30 - 4:30pm</div></div>
  <div class="abs" style="left:496px;top:730px;width:2px;height:58px;background:var(--lime)"></div>
  <div class="age" style="left:510px;top:730px"><div class="label" style="font-size:17px">12 YEARS <b>AND</b> OVER</div><div style="font-size:30px">4:45 - 5:45pm</div></div>

  <div class="strip" style="left:20px;top:811px;width:740px;height:48px;font-size:12px">
    <svg class="icon" style="margin-left:38px" width="14" height="18" viewBox="0 0 14 18"><path d="M7 0a7 7 0 0 0-7 7c0 5 7 11 7 11s7-6 7-11a7 7 0 0 0-7-7zm0 10a3 3 0 1 1 0-6 3 3 0 0 1 0 6z" fill="var(--lime)"/></svg>
    <span style="margin-left:10px;line-height:1.25">Apex Gymsports,<br>24-26 Carrow Lane Westbrook</span>
    <span style="margin-left:74px;font-size:15px">COST:</span>
    <span class="price" style="margin-left:10px;font-size:36px">$10</span>
    <span style="margin-left:8px;font-size:12px">and includes an Apex merchandise pack</span>
  </div>

  <div class="info-box" style="left:51px;top:900px;width:678px;height:84px;font-size:12px;line-height:1.35;padding-top:14px">
    <div class="q" style="font-size:15px">Unsure what cheerleading is like?</div>
    <div>Come along to our open week to try it out with our current Apex cheerleading teams. Classes are<br>available from the <span class="hl">6th-10th of December</span>. Please contact us for more information! Bookings are required.</div>
  </div>
  <div class="tag" style="left:223px;top:890px;width:338px;height:23px;font-size:12px">SEMI-COMPETITIVE TEAMS ALSO AVAILABLE</div>

  <div class="footer" style="left:51px;top:1006px;height:56px;font-size:14px">
    <span class="brand" style="font-size:20px">Apex Gymsports</span>
    <svg class="icon" style="margin-left:22px" width="16" height="16" viewBox="0 0 24 24"><path d="M6.6 10.8a15.1 15.1 0 0 0 6.6 6.6l2.2-2.2c.3-.3.7-.4 1-.2 1.1.4 2.3.6 3.6.6.6 0 1 .4 1 1V20c0 .6-.4 1-1 1A17 17 0 0 1 3 4c0-.6.4-1 1-1h3.5c.6 0 1 .4 1 1 0 1.3.2 2.5.6 3.6.1.3 0 .7-.2 1z" fill="var(--lime)"/></svg>
    <span style="margin-left:6px;font-size:20px;font-weight:800">95550182</span>
    <svg class="icon" style="margin-left:18px" width="16" height="12" viewBox="0 0 16 12"><rect x=".5" y=".5" width="15" height="11" fill="none" stroke="var(--lime)"/><path d="M.5.5 8 7 15.5.5" fill="none" stroke="var(--lime)"/></svg>
    <span style="margin-left:8px">cheer@apexgymsports.com</span>
    <svg class="icon" style="margin-left:12px" width="15" height="15" viewBox="0 0 16 16"><circle cx="8" cy="8" r="7" fill="none" stroke="var(--lime)" stroke-width="1.5"/><path d="M1 8h14M8 1c-3 3-3 11 0 14M8 1c3 3 3 11 0 14" fill="none" stroke="var(--lime)"/></svg>
    <span style="margin-left:6px">www.apexgymsports.com</span>
  </div>
</section>

<!-- ================= BANNER ================= -->
<section class="piece banner">
  <div class="photo" role="img" aria-label="Cheerleader mid-air in a toe-touch jump" style="left:44px;top:6px;width:265px;height:94px;border-radius:40px"></div>
  <div class="photo" role="img" aria-label="Cheerleading stunt group lifting a flyer, left side" style="left:0;top:89px;width:137px;height:402px"></div>
  <div class="photo" role="img" aria-label="Cheerleading pyramid and team members, right side" style="left:799px;top:0;width:181px;height:491px"></div>

  <div class="abs display year-navy" style="left:0;width:980px;text-align:center;top:22px;font-size:80px">2022</div>
  <div class="abs display title" style="left:0;width:980px;text-align:center;top:100px;font-size:48px">CHEERLEADING</div>
  <div class="abs sub" style="left:0;width:980px;text-align:center;top:152px;font-size:27px">TEAM PLACEMENTS</div>

  <div class="band" style="left:192px;top:188px;width:596px;height:50px;font-size:14px">
    <span>Try out for a cheerleading team!</span>
    <span>Everyone is welcome and will be placed on a team, regardless of skill level.</span>
  </div>

  <div class="date-box" style="left:226px;top:253px;width:70px;height:50px;font-size:24px">
    <span style="font-size:9px;margin-bottom:2px">SATURDAY</span><span>11<sup>th</sup></span><span style="font-size:8px;margin-top:1px">DECEMBER</span>
  </div>
  <div class="yr" style="left:309px;top:258px;font-size:38px">2021</div>
  <div class="age" style="left:398px;top:257px"><div class="label" style="font-size:13px">11 YEARS <b>AND</b> UNDER</div><div style="font-size:24px">3:30 - 4:30pm</div></div>
  <div class="abs" style="left:575px;top:257px;width:2px;height:44px;background:var(--lime)"></div>
  <div class="age" style="left:587px;top:257px"><div class="label" style="font-size:13px">12 YEARS <b>AND</b> OVER</div><div style="font-size:24px">4:45 - 5:45pm</div></div>

  <div class="strip" style="left:223px;top:320px;width:545px;height:29px;font-size:9px;clip-path:polygon(2% 0,100% 0,98% 100%,0 100%)">
    <svg class="icon" style="margin-left:18px" width="10" height="13" viewBox="0 0 14 18"><path d="M7 0a7 7 0 0 0-7 7c0 5 7 11 7 11s7-6 7-11a7 7 0 0 0-7-7zm0 10a3 3 0 1 1 0-6 3 3 0 0 1 0 6z" fill="var(--lime)"/></svg>
    <span style="margin-left:8px">Apex Gymsports, 24-26 Carrow Lane Westbrook</span>
    <span style="margin-left:10px;font-size:11px">COST:</span>
    <span class="price" style="margin-left:6px;font-size:26px">$10</span>
    <span style="margin-left:6px">and includes an Apex merchandise pack</span>
  </div>

  <div class="info-box" style="left:160px;top:374px;width:638px;height:53px;font-size:9px;line-height:1.3;padding-top:8px">
    <div class="q" style="font-size:11px">Unsure what cheerleading is like?</div>
    <div>Come along to our open week to try it out with our current Apex cheerleading teams. Classes are available from the <span class="hl">6th-10th of December</span>. Please<br>contact us for more information! Bookings are required.</div>
  </div>
  <div class="tag" style="left:380px;top:366px;width:218px;height:16px;font-size:9px">SEMI-COMPETITIVE TEAMS ALSO AVAILABLE</div>

  <div class="footer" style="left:184px;top:443px;width:639px;height:48px;background:var(--navy-deep);clip-path:polygon(3% 0,97% 0,100% 100%,0 100%);font-size:13px;padding-left:20px">
    <span class="brand" style="font-size:16px">Apex Gymsports</span>
    <svg class="icon" style="margin-left:14px" width="14" height="14" viewBox="0 0 24 24"><path d="M6.6 10.8a15.1 15.1 0 0 0 6.6 6.6l2.2-2.2c.3-.3.7-.4 1-.2 1.1.4 2.3.6 3.6.6.6 0 1 .4 1 1V20c0 .6-.4 1-1 1A17 17 0 0 1 3 4c0-.6.4-1 1-1h3.5c.6 0 1 .4 1 1 0 1.3.2 2.5.6 3.6.1.3 0 .7-.2 1z" fill="var(--lime)"/></svg>
    <span style="margin-left:5px;font-size:17px;font-weight:800">95550182</span>
    <svg class="icon" style="margin-left:14px" width="14" height="11" viewBox="0 0 16 12"><rect x=".5" y=".5" width="15" height="11" fill="none" stroke="var(--lime)"/><path d="M.5.5 8 7 15.5.5" fill="none" stroke="var(--lime)"/></svg>
    <span style="margin-left:6px">cheer@apexgymsports.com</span>
    <svg class="icon" style="margin-left:12px" width="13" height="13" viewBox="0 0 16 16"><circle cx="8" cy="8" r="7" fill="none" stroke="var(--lime)" stroke-width="1.5"/><path d="M1 8h14M8 1c-3 3-3 11 0 14M8 1c3 3 3 11 0 14" fill="none" stroke="var(--lime)"/></svg>
    <span style="margin-left:5px">www.apexgymsports.com</span>
  </div>
</section>

<!-- ================= SOCIAL POST A ================= -->
<section class="piece social social-a">
  <div class="photo" role="img" aria-label="Cheerleading pyramid with a flyer raising both arms" style="left:499px;top:20px;width:335px;height:764px"></div>
  <div class="photo" role="img" aria-label="Cheerleader in a mid-air split jump" style="left:362px;top:153px;width:194px;height:117px;border-radius:40px"></div>
  <div class="topbar"></div>
  <div class="panel"></div>
  <div class="abs brand" style="left:64px;top:48px;font-size:34px">Apex Gymsports</div>
  <div class="abs display year-navy" style="left:51px;top:153px;font-size:90px">2022</div>
  <div class="navy-band" style="top:254px;width:485px;height:62px"></div>
  <div class="abs display" style="left:56px;top:263px;font-size:44px;color:var(--silver);letter-spacing:2px">CHEERLEADING</div>
  <div class="abs sub dark" style="left:64px;top:328px;font-size:32px">TEAM PLACEMENTS</div>
  <div class="abs dark" style="left:64px;top:376px;font-size:17px;font-weight:700;line-height:1.25">Try out for a cheerleading team!<br>Everyone is welcome and will be placed<br>on a team, regardless of skill level.</div>
  <div class="date-card">
    <div class="day dark">SATURDAY<br><span class="num">11<sup style="font-size:15px">th</sup></span><br>DECEMBER</div>
    <div class="yr-block"><span class="yr">2021</span></div>
  </div>
  <div class="abs dark times"><div style="font-size:12px;font-weight:700">11 YEARS AND UNDER</div>3:30 - 4:30pm<div style="font-size:12px;font-weight:700;margin-top:6px">12 YEARS AND OVER</div>4:45 - 5:45pm</div>
  <div class="navy-band" style="top:553px;width:485px;height:39px"></div>
  <div class="abs" style="left:56px;top:562px;font-size:16px;font-weight:700;display:flex;align-items:center">
    <svg class="icon" width="14" height="18" viewBox="0 0 14 18"><path d="M7 0a7 7 0 0 0-7 7c0 5 7 11 7 11s7-6 7-11a7 7 0 0 0-7-7zm0 10a3 3 0 1 1 0-6 3 3 0 0 1 0 6z" fill="var(--lime)"/></svg>
    <span style="margin-left:12px">Apex Gymsports, 24-26 Carrow Lane Westbrook</span>
  </div>
  <div class="abs dark" style="left:59px;top:605px;display:flex;align-items:center;white-space:nowrap">
    <span class="display" style="font-size:34px">COST:</span>
    <span style="font-family:'Oswald',sans-serif;font-weight:600;font-size:52px;margin-left:14px;line-height:1">$10</span>
    <span style="font-size:20px;font-weight:700;margin-left:8px;line-height:1.05">and includes an Apex<br>merchandise pack</span>
  </div>
  <div class="tag" style="left:59px;top:675px;width:312px;height:23px;font-size:12px;clip-path:polygon(0 0,100% 0,96% 100%,0 100%)">SEMI-COMPETITIVE TEAMS ALSO AVAILABLE</div>
  <div class="abs dark" style="left:59px;top:706px;width:500px;font-size:11px;font-weight:600;line-height:1.25">
    <div style="font-size:14px;font-weight:800">Unsure what cheerleading is like?</div>
    Come along to our open week to try it out with our current Apex cheerleading teams.<br>Classes are available from the 6th-10th of December. Please contact us for more<br>information!
  </div>
  <div class="footer" style="left:0;top:777px;width:834px;height:54px;background:var(--navy);padding-left:59px">
    <svg class="icon" width="18" height="18" viewBox="0 0 24 24"><path d="M6.6 10.8a15.1 15.1 0 0 0 6.6 6.6l2.2-2.2c.3-.3.7-.4 1-.2 1.1.4 2.3.6 3.6.6.6 0 1 .4 1 1V20c0 .6-.4 1-1 1A17 17 0 0 1 3 4c0-.6.4-1 1-1h3.5c.6 0 1 .4 1 1 0 1.3.2 2.5.6 3.6.1.3 0 .7-.2 1z" fill="var(--lime)"/></svg>
    <span style="margin-left:12px;font-size:30px;font-weight:900">95550182</span>
    <span style="margin-left:28px;width:1px;height:34px;background:var(--white)"></span>
    <div style="margin-left:14px;font-size:15px;line-height:1.2">
      <div><svg class="icon" width="14" height="11" viewBox="0 0 16 12"><rect x=".5" y=".5" width="15" height="11" fill="none" stroke="var(--lime)"/><path d="M.5.5 8 7 15.5.5" fill="none" stroke="var(--lime)"/></svg> cheer@apexgymsports.com</div>
      <div><svg class="icon" width="13" height="13" viewBox="0 0 16 16"><circle cx="8" cy="8" r="7" fill="none" stroke="var(--lime)" stroke-width="1.5"/><path d="M1 8h14M8 1c-3 3-3 11 0 14M8 1c3 3 3 11 0 14" fill="none" stroke="var(--lime)"/></svg> www.apexgymsports.com</div>
    </div>
  </div>
</section>

<!-- ================= SOCIAL POST B ================= -->
<section class="piece social social-b">
  <div class="photo" role="img" aria-label="Cheerleading pyramid with a flyer raising both arms" style="left:499px;top:20px;width:335px;height:764px"></div>
  <div class="photo" role="img" aria-label="Cheerleader in a mid-air split jump" style="left:362px;top:153px;width:194px;height:117px;border-radius:40px"></div>
  <div class="topbar"></div>
  <div class="panel"></div>
  <div class="abs brand" style="left:64px;top:48px;font-size:34px">Apex Gymsports</div>
  <div class="abs display year" style="left:51px;top:153px;font-size:90px">2022</div>
  <div class="navy-band" style="top:254px;width:485px;height:62px"></div>
  <div class="abs display" style="left:56px;top:263px;font-size:44px;color:var(--silver);letter-spacing:2px">CHEERLEADING</div>
  <div class="abs sub dark" style="left:64px;top:328px;font-size:32px">TEAM PLACEMENTS</div>
  <div class="abs dark" style="left:64px;top:376px;font-size:17px;font-weight:700;line-height:1.25">Try out for a cheerleading team!<br>Everyone is welcome and will be placed<br>on a team, regardless of skill level.</div>
  <div class="date-card">
    <div class="day dark">SATURDAY<br><span class="num">11<sup style="font-size:15px">th</sup></span><br>DECEMBER</div>
    <div class="yr-block"><span class="yr">2021</span></div>
  </div>
  <div class="abs dark times"><div style="font-size:12px;font-weight:700">11 YEARS AND UNDER</div>3:30 - 4:30pm<div style="font-size:12px;font-weight:700;margin-top:6px">12 YEARS AND OVER</div>4:45 - 5:45pm</div>
  <div class="navy-band" style="top:553px;width:485px;height:39px"></div>
  <div class="abs" style="left:56px;top:562px;font-size:16px;font-weight:700;display:flex;align-items:center">
    <svg class="icon" width="14" height="18" viewBox="0 0 14 18"><path d="M7 0a7 7 0 0 0-7 7c0 5 7 11 7 11s7-6 7-11a7 7 0 0 0-7-7zm0 10a3 3 0 1 1 0-6 3 3 0 0 1 0 6z" fill="var(--lime)"/></svg>
    <span style="margin-left:12px">Apex Gymsports, 24-26 Carrow Lane Westbrook</span>
  </div>
  <div class="abs dark" style="left:59px;top:605px;display:flex;align-items:center;white-space:nowrap">
    <span class="display" style="font-size:34px">COST:</span>
    <span style="font-family:'Oswald',sans-serif;font-weight:600;font-size:52px;margin-left:14px;line-height:1">$10</span>
    <span style="font-size:20px;font-weight:700;margin-left:8px;line-height:1.05">and includes an Apex<br>merchandise pack</span>
  </div>
  <div class="tag" style="left:59px;top:675px;width:312px;height:23px;font-size:12px;clip-path:polygon(0 0,100% 0,96% 100%,0 100%)">SEMI-COMPETITIVE TEAMS ALSO AVAILABLE</div>
  <div class="abs dark" style="left:59px;top:706px;width:500px;font-size:11px;font-weight:600;line-height:1.25">
    <div style="font-size:14px;font-weight:800">Unsure what cheerleading is like?</div>
    Come along to our open week to try it out with our current Apex cheerleading teams.<br>Classes are available from the 6th-10th of December. Please contact us for more<br>information!
  </div>
  <div class="footer" style="left:0;top:777px;width:834px;height:54px;background:var(--navy);padding-left:59px">
    <svg class="icon" width="18" height="18" viewBox="0 0 24 24"><path d="M6.6 10.8a15.1 15.1 0 0 0 6.6 6.6l2.2-2.2c.3-.3.7-.4 1-.2 1.1.4 2.3.6 3.6.6.6 0 1 .4 1 1V20c0 .6-.4 1-1 1A17 17 0 0 1 3 4c0-.6.4-1 1-1h3.5c.6 0 1 .4 1 1 0 1.3.2 2.5.6 3.6.1.3 0 .7-.2 1z" fill="var(--lime)"/></svg>
    <span style="margin-left:12px;font-size:30px;font-weight:900">95550182</span>
    <span style="margin-left:28px;width:1px;height:34px;background:var(--white)"></span>
    <div style="margin-left:14px;font-size:15px;line-height:1.2">
      <div><svg class="icon" width="14" height="11" viewBox="0 0 16 12"><rect x=".5" y=".5" width="15" height="11" fill="none" stroke="var(--lime)"/><path d="M.5.5 8 7 15.5.5" fill="none" stroke="var(--lime)"/></svg> cheer@apexgymsports.com</div>
      <div><svg class="icon" width="13" height="13" viewBox="0 0 16 16"><circle cx="8" cy="8" r="7" fill="none" stroke="var(--lime)" stroke-width="1.5"/><path d="M1 8h14M8 1c-3 3-3 11 0 14M8 1c3 3 3 11 0 14" fill="none" stroke="var(--lime)"/></svg> www.apexgymsports.com</div>
    </div>
  </div>
</section>

</body>
</html>
```